Kivo Campaign Flyer

Tobu is a not-for-profit college planning organization serving the students of Louisiana's public and private high schools.

Tobu will offer Louisiana high school seniors, aged 17-19, the opportunity to compete for a free Kivo by registering and completing a brief survey on our webpage by March 1st to be eligible for this random drawing.

As a result, we are soliciting designs for an age-appropriate, innovative design idea to promote this program. The winning design will be printed as a 5-3/4” x 7-3/4” flyer which will be distributed to Louisiana high school seniors and guidance counselors, encouraging them to participate.

```html
<!DOCTYPE html>
<html lang="en">
<head>
<meta charset="utf-8">
<title>Win a Kivo – askTobu.org</title>
<link rel="stylesheet" href="https://fonts.googleapis.com/css2?family=Open+Sans:wght@300;400;700&display=swap">
<style>
  :root {
    --orange: #d96a04;
    --blue: #2155de;
    --lime: #b3f500;
    --green: #a1e500;
    --navy: #0d1f72;
    --red: #e0261d;
    --white: #ffffff;
  }
  * { margin: 0; padding: 0; box-sizing: border-box; }
  html, body { width: 890px; height: 1200px; overflow: hidden; background: var(--white); }
  .flyer {
    position: relative;
    width: 890px;
    height: 1200px;
    overflow: hidden;
    background: var(--white);
    font-family: "Open Sans", sans-serif;
  }
  .band { position: absolute; }
  .band--orange { background: var(--orange); }
  .band--blue { background: var(--blue); }
  .band--lime { background: var(--lime); }

  .brand-disc {
    position: absolute;
    left: 389px; top: 165px;
    width: 404px; height: 404px;
    border-radius: 50%;
    background: var(--green);
  }
  .brand-name {
    position: absolute;
    left: 300px; top: 318px;
    font-size: 84px;
    font-weight: 400;
    color: var(--navy);
    letter-spacing: -1px;
    line-height: 1;
  }

  .step { position: absolute; white-space: nowrap; line-height: 1; }
  .step--visit {
    left: 434px; top: 620px;
    font-size: 22px; font-weight: 400; color: var(--blue);
  }
  .step--visit .accent { color: var(--red); }
  .step--survey {
    left: 406px; top: 689px;
    font-size: 18px; font-weight: 700; color: var(--lime); line-height: 1.2;
  }
  .step--prize {
    left: 348px; top: 778px;
    font-size: 30px; font-weight: 300; color: var(--white);
  }
  .step--prize .accent { color: var(--lime); }

  .headline {
    position: absolute;
    left: 0; width: 890px; top: 935px;
    text-align: center;
    font-size: 128px;
    font-weight: 300;
    line-height: 1;
    letter-spacing: 2px;
    white-space: nowrap;
  }
  .headline .w1 { color: var(--orange); }
  .headline .w2 { color: var(--blue); }
  .headline .w3 { color: var(--lime); }
</style>
</head>
<body>
  <main class="flyer">
    <!-- left nested L bands -->
    <div class="band band--orange" style="left:73px; top:0; width:61px; height:835px;"></div>
    <div class="band band--orange" style="left:73px; top:770px; width:469px; height:65px;"></div>

    <div class="band band--blue" style="left:152px; top:0; width:61px; height:753px;"></div>
    <div class="band band--blue" style="left:152px; top:689px; width:469px; height:64px;"></div>

    <div class="band band--lime" style="left:235px; top:0; width:61px; height:671px;"></div>
    <div class="band band--lime" style="left:235px; top:607px; width:468px; height:64px;"></div>

    <!-- right edge stripe -->
    <div class="band band--lime" style="left:864px; top:0; width:26px; height:342px;"></div>
    <div class="band band--blue" style="left:864px; top:342px; width:26px; height:350px;"></div>
    <div class="band band--orange" style="left:864px; top:692px; width:26px; height:351px;"></div>

    <!-- brand -->
    <div class="brand-disc"></div>
    <div class="brand-name">askTobu.org</div>

    <!-- steps -->
    <p class="step step--visit"><span class="accent">Visit</span> www.asktobu.org</p>
    <p class="step step--survey">Complete a survey<br>Before march 1st</p>
    <p class="step step--prize">Win <span class="accent">A</span> Kivo</p>

    <h1 class="headline"><span class="w1">WIN</span> <span class="w2">A</span> <span class="w3">KIVO</span></h1>
  </main>
</body>
</html>
```